Power Point make-over

We need an immediate turn around on this power point project. The presentation needs a make-over. The project includes:
1. Creating uniformity in font, colors, etc.
2. Enhancing charts and graphs.
3. Producing a better layout.
4. Some sildes can be combines.
5. The "notes" on certain slides should appear on the slide.
6. Add Tern Ridge Consulting logo- maybe as footer.

Finally- Each section (Chart your Path- Talent Compass- QRN exercise) of the power point is used in the same presentation so it needs uniformity but it does not require a segway. These exercises are also used individually for shorter presentations, so I need them to be able to stand alone. Ultimately, I need to be able to edit the power point as needed.

Target Market(s)

CEO, Executives

Industry/Entity Type

Consulting

Requirements
Must have
• The project includes:

Nice to have
• I prefer a plain white background.

```html
<!DOCTYPE html>
<html lang="en">
<head>
<meta charset="utf-8">
<title>Chart/Graph Style</title>
<link href="https://fonts.googleapis.com/css2?family=Archivo:wdth,wght@62..125,800&family=Caladea&display=swap" rel="stylesheet">
<style>
  :root {
    --bg: #f7f8f8;
    --title-green: #116b4f;
    --series-1: #136fc7;
    --series-2: #049dd9;
    --series-3: #0dd1d8;
    --grid: #8a8a8a;
    --axis-text: #000000;
    --band-left: #7fe0ec;
    --band-mid: #a6d8ec;
    --band-right: #6cc4e8;
    --logo-panel: #ffffff;
  }
  html, body {
    margin: 0;
    padding: 0;
    width: 1200px;
    height: 902px;
    overflow: hidden;
    background: var(--bg);
  }
  .slide {
    position: relative;
    width: 1200px;
    height: 902px;
    background: var(--bg);
    overflow: hidden;
  }
  .header-band {
    position: absolute;
    top: 0;
    left: 0;
    width: 1200px;
    height: 135px;
    background:
      linear-gradient(to bottom, rgba(247,248,248,0) 0%, rgba(247,248,248,0) 45%, var(--bg) 100%),
      linear-gradient(to right, var(--band-left) 0%, var(--band-mid) 50%, var(--band-right) 100%);
  }
  .slide-title {
    position: absolute;
    left: 58px;
    top: 178px;
    margin: 0;
    font-family: "Archivo", "Arial Black", sans-serif;
    font-weight: 800;
    font-stretch: 88%;
    font-size: 54px;
    line-height: 1;
    letter-spacing: -0.5px;
    color: var(--title-green);
  }
  .bar-chart {
    position: absolute;
    top: 0;
    left: 0;
  }
  .bar-chart text {
    font-family: "Caladea", "Cambria", serif;
    font-size: 26px;
    fill: var(--axis-text);
    font-variant-numeric: oldstyle-nums;
  }
  .bar-chart .x-labels text,
  .bar-chart .legend text {
    font-size: 28px;
  }
  .gridline { stroke: var(--grid); stroke-width: 1; }
  .bar-s1 { fill: var(--series-1); }
  .bar-s2 { fill: var(--series-2); }
  .bar-s3 { fill: var(--series-3); }
  .brand-footer {
    position: absolute;
    left: 25px;
    top: 785px;
    width: 316px;
    height: 102px;
    background: var(--logo-panel);
    display: flex;
    align-items: center;
    gap: 14px;
    padding-left: 12px;
    box-sizing: border-box;
  }
  .brand-mark {
    width: 62px;
    height: 62px;
    border-radius: 50%;
    background: var(--title-green);
    flex: none;
  }
  .brand-name {
    font-family: "Archivo", "Arial Black", sans-serif;
    font-weight: 800;
    font-size: 22px;
    line-height: 1.1;
    color: var(--title-green);
  }
</style>
</head>
<body>
<main class="slide">
  <div class="header-band" role="img" aria-label="Decorative flowing blue wave banner across the top of the slide"></div>

  <h1 class="slide-title">CHART/GRAPH STYLE</h1>

  <svg class="bar-chart" width="1200" height="720" viewBox="0 0 1200 720" role="img" aria-label="Clustered bar chart of three series across four categories">
    <g class="grid">
      <line class="gridline" x1="107" y1="280.6" x2="970" y2="280.6"/>
      <line class="gridline" x1="107" y1="337.5" x2="970" y2="337.5"/>
      <line class="gridline" x1="107" y1="394.4" x2="970" y2="394.4"/>
      <line class="gridline" x1="107" y1="451.3" x2="970" y2="451.3"/>
      <line class="gridline" x1="107" y1="508.2" x2="970" y2="508.2"/>
      <line class="gridline" x1="107" y1="565.1" x2="970" y2="565.1"/>
      <line class="gridline" x1="107" y1="622" x2="970" y2="622"/>
      <line class="gridline" x1="115" y1="280.6" x2="115" y2="630"/>
      <line class="gridline" x1="328.75" y1="622" x2="328.75" y2="630"/>
      <line class="gridline" x1="542.5" y1="622" x2="542.5" y2="630"/>
      <line class="gridline" x1="756.25" y1="622" x2="756.25" y2="630"/>
      <line class="gridline" x1="970" y1="622" x2="970" y2="630"/>
    </g>
    <g class="y-labels" text-anchor="end">
      <text x="86" y="290">6</text>
      <text x="86" y="347">5</text>
      <text x="86" y="404">4</text>
      <text x="86" y="461">3</text>
      <text x="86" y="518">2</text>
      <text x="86" y="575">1</text>
      <text x="86" y="632">0</text>
    </g>
    <g class="bars">
      <rect class="bar-s1" x="150" y="377.3" width="47" height="244.7"/>
      <rect class="bar-s2" x="197" y="485.4" width="48" height="136.6"/>
      <rect class="bar-s3" x="245" y="508.2" width="47" height="113.8"/>

      <rect class="bar-s1" x="363.75" y="479.75" width="47" height="142.25"/>
      <rect class="bar-s2" x="410.75" y="371.6" width="48" height="250.4"/>
      <rect class="bar-s3" x="458.75" y="508.2" width="47" height="113.8"/>

      <rect class="bar-s1" x="577.5" y="422.9" width="47" height="199.1"/>
      <rect class="bar-s2" x="624.5" y="519.6" width="48" height="102.4"/>
      <rect class="bar-s3" x="672.5" y="451.3" width="47" height="170.7"/>

      <rect class="bar-s1" x="791.25" y="366" width="47" height="256"/>
      <rect class="bar-s2" x="838.25" y="462.7" width="48" height="159.3"/>
      <rect class="bar-s3" x="886.25" y="337.5" width="47" height="284.5"/>
    </g>
    <g class="x-labels" text-anchor="middle">
      <text x="222" y="670">Category 1</text>
      <text x="435.6" y="670">Category 2</text>
      <text x="649.4" y="670">Category 3</text>
      <text x="863.1" y="670">Category 4</text>
    </g>
    <g class="legend">
      <rect class="bar-s1" x="1001" y="417" width="14" height="14"/>
      <text x="1024" y="434">Series 1</text>
      <rect class="bar-s2" x="1001" y="463" width="14" height="14"/>
      <text x="1024" y="480">Series 2</text>
      <rect class="bar-s3" x="1001" y="509" width="14" height="14"/>
      <text x="1024" y="526">Series 3</text>
    </g>
  </svg>

  <footer class="brand-footer">
    <span class="brand-mark"></span>
    <span class="brand-name">TERN RIDGE<br>CONSULTING</span>
  </footer>
</main>
</body>
</html>
```